Small boutique multi-family apartment developer needs premium website design.

We are a growing real estate development company specializing in multi family apartment development. Our company Mireval Stone Development focuses on passive real estate investors looking to maximize their current real estate portfolio by allowing us to develop and reposition their current properties allowing them more cashflow while we are also able to take over the management of their asset in order to ensure optimal performance on a consistent basis.

```html
<!DOCTYPE html>
<html lang="en">
<head>
<meta charset="utf-8">
<title>Mireval Stone Development</title>
<link href="https://fonts.googleapis.com/css2?family=Montserrat:wght@400;500;600;700&family=Orbitron:wght@500;600&family=Poppins:wght@400;500;600&display=swap" rel="stylesheet">
<style>
:root{
  --blue:#6391e8;
  --blue-deep:#3f64c4;
  --navy:#2d4a9a;
  --ink:#222;
  --text:#333;
  --pale:#eef3fb;
  --dark:#333335;
  --footer:#4a6fc9;
  --white:#fff;
  --star:#f5c518;
}
*{margin:0;padding:0;box-sizing:border-box}
html,body{width:1200px;height:4323px;overflow:hidden}
body{position:relative;background:var(--white);font-family:"Montserrat",sans-serif;color:var(--text)}
.abs{position:absolute}
.display{font-family:"Orbitron",sans-serif;font-weight:500}
.btn{position:absolute;display:flex;align-items:center;justify-content:center;background:var(--blue);color:var(--white);border-radius:6px;font-family:"Poppins",sans-serif;font-weight:500;font-size:13px}
.photo{position:absolute}

/* header */
.site-header{position:absolute;left:0;top:0;width:1200px;height:72px;background:var(--white);border-bottom:2px solid #3d4f7a;z-index:3}
.brand{position:absolute;left:140px;top:14px;font-family:"Montserrat",sans-serif;font-weight:700;font-size:34px;color:var(--blue);letter-spacing:1px}
.nav a{position:absolute;top:28px;font-size:13px;color:var(--ink);text-decoration:none}
.nav .btn{top:20px;left:965px;width:93px;height:34px}

/* hero */
.hero{position:absolute;left:0;top:72px;width:1200px;height:460px;background:linear-gradient(90deg,#f3f7fd 0%,#e6eefa 45%,#4d86d8 62%,#2f6ccd 80%,#7aa9e6 100%)}
.hero h1{position:absolute;left:0;width:710px;top:118px;text-align:center;font-size:50px;font-weight:700;color:var(--navy);letter-spacing:1px}
.hero p{position:absolute;left:0;width:675px;top:185px;text-align:center;font-size:18px;line-height:21px;color:#3d5890}
.hero .btn{left:264px;top:258px;width:147px;height:42px;border-radius:2px;font-family:"Montserrat",sans-serif;font-weight:400;font-size:14px}

/* about */
.about-photo{left:135px;top:647px;width:423px;height:406px;border-radius:44px;background:linear-gradient(135deg,#e9e6e2,#c9b8a8 50%,#8a6f5c);border:5px solid var(--blue)}
.section-title{position:absolute;font-size:34px;line-height:42px;color:var(--ink)}
.section-title span{color:var(--blue)}
.body-copy{position:absolute;font-size:13px;line-height:19px;color:var(--text)}

/* expertise */
.expertise{position:absolute;left:0;top:1170px;width:1200px;height:642px;background:var(--blue)}
.expertise h2{position:absolute;left:0;width:1200px;top:76px;text-align:center;font-size:34px;line-height:42px;color:var(--white)}
.expertise .lead{position:absolute;left:0;width:1200px;top:178px;text-align:center;font-size:13px;line-height:19px;color:var(--white)}
.card{position:absolute;top:254px;width:296px;height:308px;background:var(--white);border-radius:18px}
.card.is-active{box-shadow:inset 0 5px 0 var(--blue-deep)}
.card svg{position:absolute;left:42px;top:42px}
.card h3{position:absolute;left:44px;top:130px;font-family:"Orbitron",sans-serif;font-weight:500;font-size:19px;color:var(--ink)}
.card p{position:absolute;left:44px;top:174px;width:210px;font-size:13px;line-height:19px;color:var(--text)}

/* investment */
.invest-photo{left:640px;top:1897px;width:425px;height:405px;border-radius:40px;background:linear-gradient(120deg,#6f9b4e,#e6d49a 45%,#c69a62 75%,#8f6b45);border-right:6px solid var(--blue);border-bottom:6px solid var(--blue)}

/* testimonials */
.testimonials{position:absolute;left:0;top:2445px;width:1200px;height:545px}
.testimonials h2{position:absolute;left:0;width:1200px;top:82px;text-align:center;font-size:33px;color:var(--white)}
.quote-card{position:absolute;left:286px;top:187px;width:627px;height:273px;background:var(--white);border:2px solid var(--blue);border-radius:16px}
.quote-card p{position:absolute;left:80px;width:463px;top:44px;text-align:center;font-size:12px;line-height:19px;color:var(--text)}
.quote-mark{position:absolute;left:566px;top:148px;z-index:2}
.avatar{position:absolute;left:291px;top:160px;width:42px;height:42px;border-radius:50%;background:linear-gradient(#d8a07a,#a6683f)}
.quote-card .name{position:absolute;left:0;width:623px;top:211px;text-align:center;font-size:13px;font-weight:600;color:var(--ink)}
.stars{position:absolute;left:272px;top:230px}
.arrow-btn{position:absolute;width:36px;height:36px;border-radius:50%;border:2px solid var(--blue-deep);background:var(--white)}

/* portfolio */
.portfolio-tile{position:absolute;width:234px;height:205px}

/* cta */
.cta h2{position:absolute;left:142px;top:3788px;font-size:32px;line-height:40px;color:var(--white)}
.cta .btn{left:142px;top:3903px;width:155px;height:34px;background:var(--white);color:var(--ink);font-size:12px;font-weight:600}
.cta p{position:absolute;left:630px;width:315px;top:3790px;text-align:right;font-size:13px;line-height:19px;color:var(--white)}

/* footer */
.site-footer{position:absolute;left:0;top:4000px;width:1200px;height:285px;background:var(--footer)}
.site-footer .brand{left:140px;top:68px;color:var(--white)}
.social{position:absolute;top:146px;width:30px;height:30px;border-radius:50%;border:2px solid var(--white)}
.site-footer h4{position:absolute;top:70px;font-family:"Orbitron",sans-serif;font-weight:500;font-size:19px;color:var(--white)}
.links a{position:absolute;left:512px;font-size:13px;color:var(--white);text-decoration:none}
.contact-line{position:absolute;left:864px;font-size:13px;line-height:19px;color:var(--white)}
.contact-icon{position:absolute;left:828px}
.copyright{position:absolute;left:0;top:4285px;width:1200px;height:38px;background:var(--dark);color:var(--white);text-align:center;font-size:12px;line-height:38px}
</style>
</head>
<body>

<header class="site-header">
  <div class="brand">MIREVAL</div>
  <nav class="nav">
    <a style="left:626px">Home</a>
    <a style="left:701px">About</a>
    <a style="left:777px">Services</a>
    <a style="left:866px">Properties</a>
    <a class="btn">Contact</a>
  </nav>
</header>

<section class="hero" role="img" aria-label="Upward view of glass high-rise towers against a pale sky">
  <h1>MAXIMIZING RETURNS</h1>
  <p>Partner with Mireval Stone Development to optimize<br>your real estate portfolio</p>
  <a class="btn">CONTACT US</a>
  <svg class="abs" style="left:0;top:330px" width="1200" height="132" viewBox="0 0 1200 132">
    <path d="M0 62 C170 20 330 30 420 70 C520 112 600 60 760 70 C900 80 1000 30 1200 0 L1200 132 L0 132Z" fill="#fff"/>
  </svg>
</section>

<!-- about -->
<div class="photo about-photo" role="img" aria-label="Team of young colleagues smiling around a laptop at a meeting table"></div>
<h2 class="section-title display" style="left:645px;top:694px">About <span>Mireval Stone<br>Development</span></h2>
<p class="body-copy" style="left:645px;top:806px;width:410px">We are committed to creating innovative and sustainable multi-family developments that enhance community living. Guided by our core values of quality, integrity, and customer satisfaction, we leverage our extensive experience to build homes that meet the needs of modern residents while fostering vibrant communities.</p>
<a class="btn" style="left:645px;top:958px;width:110px;height:34px">Read More</a>

<!-- expertise -->
<section class="expertise">
  <h2 class="display">Our Expertise in Multi-Family<br>Apartment Development</h2>
  <p class="lead">We specialize in developing and repositioning properties to increase cash flow and optimize performance. Our<br>services are designed to help you achieve your real estate goals.</p>

  <div class="card" style="left:141px">
    <svg width="70" height="66" viewBox="0 0 70 66" fill="none" stroke="#2d4a9a" stroke-width="2.5">
      <path d="M10 64V6M4 12h56M10 6l14 6M48 12v14"/><rect x="30" y="30" width="14" height="34"/><rect x="44" y="38" width="20" height="26"/><path d="M50 46h8M50 54h8M35 38h4M35 46h4"/>
    </svg>
    <h3>Development</h3>
    <p>Lorem Ipsum is simply dummy text of the printing and typesetting industry. Lorem Ipsum has been the industry's standard dummy...</p>
  </div>
  <div class="card is-active" style="left:452px">
    <svg width="70" height="66" viewBox="0 0 70 66" fill="none" stroke="#2d4a9a" stroke-width="2.5">
      <circle cx="54" cy="14" r="8"/><path d="M54 22v8M4 30h40v32H4zM14 38h6M14 48h6M28 38h6M28 48h6M44 40h22v22H44"/>
    </svg>
    <h3>Repositioning</h3>
    <p>Lorem Ipsum is simply dummy text of the printing and typesetting industry. Lorem Ipsum has been the industry's standard dummy...</p>
  </div>
  <div class="card" style="left:763px">
    <svg width="70" height="66" viewBox="0 0 70 66" fill="none" stroke="#2d4a9a" stroke-width="2.5">
      <rect x="14" y="4" width="40" height="30" rx="3"/><path d="M20 14l3 3 5-6M32 14h16M20 24l3 3 5-6M32 24h16M4 44l14-8 14 10 12-8 20 10M18 50l10 8M26 46l10 8"/>
    </svg>
    <h3>Management</h3>
    <p>Lorem Ipsum is simply dummy text of the printing and typesetting industry. Lorem Ipsum has been the industry's standard dummy...</p>
  </div>
</section>

<!-- investment -->
<h2 class="section-title display" style="left:142px;top:1910px">Investment<br><span>Opportunities</span></h2>
<p class="body-copy" style="left:142px;top:2021px;width:415px">Investing with Mireval Stone Development offers the potential for strong returns through strategic, high-quality real estate projects. Our deep market expertise and commitment to innovation ensure each investment is positioned for growth and resilience. With a focus on sustainable development and maximizing value, we provide investors with opportunities for steady income, capital appreciation, and long-term financial security. Partner with Mireval Stone Development and benefit from a proven track record, transparent communication, and a dedication to delivering exceptional results.</p>
<a class="btn" style="left:142px;top:2250px;width:95px;height:33px">Contact</a>
<div class="photo invest-photo" role="img" aria-label="Hand stacking coins beside a small wooden model house"></div>

<!-- testimonials -->
<section class="testimonials">
  <svg class="abs" style="left:0;top:0" width="1200" height="545" viewBox="0 0 1200 545">
    <path d="M0 0 C150 0 300 60 420 150 C520 230 720 400 690 515 C670 560 560 540 400 540 L0 540Z" fill="#eef3fb"/>
    <defs><linearGradient id="bldg" x1="0" y1="0" x2="1" y2="1"><stop offset="0" stop-color="#5c80d6"/><stop offset="0.6" stop-color="#4d6fc7"/><stop offset="1" stop-color="#7f9fdd"/></linearGradient></defs>
    <path d="M305 0 L1200 0 L1200 545 L790 545 C700 520 600 420 520 330 C420 220 280 120 275 40 C272 12 285 0 305 0Z" fill="url(#bldg)" role="img" aria-label="Blue-tinted view of modern apartment buildings"/>
  </svg>
  <h2 class="display">What Our Investors Say</h2>
  <div class="quote-card">
    <p>Lorem ipsum dolor sit amet, consectetur adipiscing elit. Donec vitae hendrerit orci. Donec nec laoreet metus. In tincidunt bibendum libero, vel faucibus est varius malesuada. Pellentesque nisi arcu, congue in aliquam nec, blandit nec leo. Nullam sollicitudin commodo suscipit. Etiam eu ultrices enim. Aenean condimentum viverra ex.</p>
    <div class="avatar" role="img" aria-label="Investor portrait"></div>
    <div class="name">Lena Ortiz</div>
    <svg class="stars" width="80" height="14" viewBox="0 0 80 14" fill="#f5c518">
      <g id="st"><path d="M7 0l2 4.6 5 .5-3.8 3.3 1.1 4.9L7 10.8 2.7 13.3l1.1-4.9L0 5.1l5-.5z"/></g>
      <use href="#st" x="16"/><use href="#st" x="32"/><use href="#st" x="48"/><use href="#st" x="64"/>
    </svg>
  </div>
  <svg class="quote-mark" width="68" height="58" viewBox="0 0 68 58" fill="#6391e8">
    <path d="M0 58V30C0 12 10 2 28 0v10C18 13 14 20 14 28h14v30zM38 58V30C38 12 48 2 66 0v10C56 13 52 20 52 28h14v30z"/>
  </svg>
  <div class="arrow-btn" style="left:220px;top:309px"><svg width="32" height="32" viewBox="0 0 32 32"><path d="M18 10l-6 6 6 6" stroke="#2d4a9a" stroke-width="2.5" fill="none"/></svg></div>
  <div class="arrow-btn" style="left:942px;top:309px;border-color:#fff"><svg width="32" height="32" viewBox="0 0 32 32"><path d="M14 10l6 6-6 6" stroke="#222" stroke-width="2.5" fill="none"/></svg></div>
</section>

<!-- portfolio -->
<h2 class="section-title display" style="left:0;width:1200px;top:3066px;text-align:center">Our <span>Portfolio</span></h2>
<p class="body-copy" style="left:0;width:1200px;top:3138px;text-align:center">Explore our current and upcoming properties, showcasing our expertise<br>in multi-family apartment development.</p>
<div class="portfolio-tile" style="left:0;top:3212px;background:linear-gradient(150deg,#b9c4cc,#7e6f60 60%,#4e5a42)" role="img" aria-label="Apartment block with balconies and trees"></div>
<div class="portfolio-tile" style="left:0;top:3422px;background:linear-gradient(160deg,#dfe5ea,#5b5f66 55%,#2f3338)" role="img" aria-label="Tall dark apartment tower"></div>
<div class="portfolio-tile" style="left:241px;top:3248px;background:linear-gradient(150deg,#f4f4f2,#a46a52 55%,#6c4a3b)" role="img" aria-label="Brick apartment building corner"></div>
<div class="portfolio-tile" style="left:241px;top:3458px;background:linear-gradient(180deg,#9ec3ea,#d6b994 55%,#6f7c55)" role="img" aria-label="Waterfront apartment complex"></div>
<div class="portfolio-tile" style="left:483px;top:3212px;background:linear-gradient(180deg,#a9c8ea,#8696a8 45%,#6e6a62)" role="img" aria-label="Aerial view of a city district"></div>
<div class="portfolio-tile" style="left:483px;top:3422px;background:linear-gradient(180deg,#cfe0f2,#4a4d4f 55%,#7e8b6a)" role="img" aria-label="Modern low-rise apartment blocks"></div>
<div class="portfolio-tile" style="left:724px;top:3248px;background:linear-gradient(120deg,#f3efe9,#c9a37a 50%,#efeae4)" role="img" aria-label="Close view of beige apartment balconies"></div>
<div class="portfolio-tile" style="left:724px;top:3458px;background:linear-gradient(160deg,#e6ecf2,#8a7967 50%,#4f4a40)" role="img" aria-label="Stacked apartment facade"></div>
<div class="portfolio-tile" style="left:965px;top:3212px;background:linear-gradient(180deg,#3f7fd2,#d6b8a8 45%,#7a6a3e 75%,#4e5d6c)" role="img" aria-label="Apartment towers across a lake"></div>
<div class="portfolio-tile" style="left:965px;top:3422px;background:linear-gradient(150deg,#b35b3c,#7e3c2c 55%,#4a3f44)" role="img" aria-label="Red brick apartment block with autumn trees"></div>

<!-- call to action -->
<section class="cta">
  <svg class="abs" style="left:0;top:3750px" width="1200" height="232" viewBox="0 0 1200 232">
    <defs><linearGradient id="street" x1="0" y1="0" x2="1" y2="0"><stop offset="0" stop-color="#4a73c8"/><stop offset="0.6" stop-color="#5a86d6"/><stop offset="1" stop-color="#b8a98a"/></linearGradient></defs>
    <path d="M572 0 L1200 0 L1200 232 L805 232 C760 200 640 60 572 0Z" fill="url(#street)" role="img" aria-label="Row of colourful townhouses under a blue sky"/>
    <path d="M0 0 L530 0 C610 40 700 150 770 210 C790 228 770 232 740 232 L0 232Z" fill="#333335"/>
  </svg>
  <h2 class="display">Ready to Transform<br>Your Portfolio?</h2>
  <a class="btn">Get Started Today</a>
  <p>Contact us to learn more about our services and how we can help you maximize your real estate portfolio.</p>
</section>

<!-- footer -->
<footer class="site-footer">
  <div class="brand">MIREVAL</div>
  <span class="social" style="left:141px"></span>
  <span class="social" style="left:186px"></span>
  <span class="social" style="left:231px"></span>
  <span class="social" style="left:276px"></span>

  <h4 style="left:512px">Quick Links</h4>
  <nav class="links">
    <a style="top:110px">Home</a>
    <a style="top:140px">About</a>
    <a style="top:170px">Services</a>
    <a style="top:200px">Properties</a>
    <a style="top:230px">Contact</a>
  </nav>

  <h4 style="left:828px">Follow us</h4>
  <svg class="contact-icon" style="top:108px" width="16" height="22" viewBox="0 0 16 22"><path d="M8 0a8 8 0 0 0-8 8c0 6 8 14 8 14s8-8 8-14a8 8 0 0 0-8-8zm0 11a3 3 0 1 1 0-6 3 3 0 0 1 0 6z" fill="#fff"/></svg>
  <p class="contact-line" style="top:106px">123 Lorem Ipsum has been the<br>industry's standard..</p>
  <svg class="contact-icon" style="top:173px" width="20" height="20" viewBox="0 0 20 20"><path d="M4 1l3 4-2 2c1 3 4 6 7 7l2-2 4 3-2 3C9 18 2 11 1 3z" fill="none" stroke="#fff" stroke-width="1.5"/></svg>
  <p class="contact-line" style="top:174px">0145 672 390</p>
  <svg class="contact-icon" style="top:222px" width="20" height="16" viewBox="0 0 20 16"><rect x="1" y="1" width="18" height="14" fill="none" stroke="#fff" stroke-width="1.5"/><path d="M1 1l9 8 9-8" fill="none" stroke="#fff" stroke-width="1.5"/></svg>
  <p class="contact-line" style="top:220px">info@mirevalstone.com</p>
</footer>
<div class="copyright">© Copyright 2024 Mireval Stone Development. All Rights Reserved.</div>

</body>
</html>
```